Good Morning Banner

We need a banner design (20.4 x 10.14) with the words 'Good Morning' as the main feature and the words 'Prophet K.O. Adelani' underneath. Attached is an example but let your creative juices flow!

Target Market(s)

Christian

```html
<!DOCTYPE html>
<html lang="en">
<head>
<meta charset="UTF-8">
<title>Good Morning Banner</title>
<link href="https://fonts.googleapis.com/css2?family=Bebas+Neue&family=Oswald:wght@400&family=Varela+Round&display=swap" rel="stylesheet">
<style>
  :root {
    --headline-yellow: #f7e01a;
    --headline-white: #ffffff;
    --bar-navy: rgba(20, 30, 45, 0.88);
    --footer-yellow: #f2e23a;
    --photo-navy: #1d2c4a;
    --photo-teal: #3e7f86;
    --photo-sand: #c9b48a;
    --photo-sky: #6d93c4;
  }
  html, body {
    margin: 0;
    padding: 0;
    width: 1200px;
    height: 597px;
    overflow: hidden;
    background: #ffffff;
  }
  .banner {
    position: relative;
    width: 1200px;
    height: 597px;
    overflow: hidden;
    font-family: "Varela Round", sans-serif;
  }
  .banner__photo {
    position: absolute;
    inset: 0;
    background:
      radial-gradient(ellipse 320px 260px at 560px 120px, rgba(214, 190, 140, 0.85), transparent 70%),
      radial-gradient(ellipse 260px 300px at 700px 420px, rgba(200, 170, 140, 0.7), transparent 70%),
      linear-gradient(90deg, var(--photo-navy) 0%, #264a5c 22%, var(--photo-teal) 36%, var(--photo-sand) 50%, #5c8a80 66%, #2e5a5a 80%, var(--photo-sky) 100%);
  }
  .headline {
    position: absolute;
    top: 98px;
    left: 34px;
    margin: 0;
    font-family: "Bebas Neue", sans-serif;
    font-weight: 400;
    font-size: 212px;
    line-height: 1;
    letter-spacing: 4px;
    white-space: nowrap;
  }
  .headline__good { color: var(--headline-yellow); }
  .headline__morning { color: var(--headline-white); margin-left: 40px; }
  .byline {
    position: absolute;
    right: 66px;
    top: 294px;
    margin: 0;
    font-family: "Oswald", sans-serif;
    font-weight: 400;
    font-size: 30px;
    line-height: 1;
    letter-spacing: 3px;
    color: var(--headline-white);
    text-transform: uppercase;
  }
  .footer-bar {
    position: absolute;
    left: 0;
    right: 0;
    bottom: 0;
    height: 56px;
    background: var(--bar-navy);
    color: var(--footer-yellow);
    font-size: 19px;
    letter-spacing: 2px;
  }
  .footer-bar__brand {
    position: absolute;
    left: 54px;
    top: 17px;
  }
  .footer-bar__item {
    position: absolute;
    top: 11px;
    display: flex;
    align-items: center;
    gap: 14px;
    color: var(--footer-yellow);
  }
  .footer-bar__item--web { left: 650px; }
  .footer-bar__item--social { left: 958px; }
  .footer-bar__icon {
    width: 34px;
    height: 34px;
    display: block;
  }
</style>
</head>
<body>
  <div class="banner">
    <div class="banner__photo" role="img" aria-label="Photograph of people shaking hands outdoors while holding leaflets, softened with bokeh light"></div>

    <h1 class="headline"><span class="headline__good">Good</span><span class="headline__morning">Morning</span></h1>
    <p class="byline">Prophet K.O. Adelani</p>

    <div class="footer-bar">
      <span class="footer-bar__brand">graceharbour.tv</span>
      <span class="footer-bar__item footer-bar__item--web">
        <svg class="footer-bar__icon" viewBox="0 0 34 34" aria-hidden="true">
          <g fill="none" stroke="#ffffff" stroke-width="1.6">
            <circle cx="17" cy="17" r="15"/>
            <ellipse cx="17" cy="17" rx="6.5" ry="15"/>
            <line x1="2" y1="17" x2="32" y2="17"/>
            <path d="M5 9.5 H29 M5 24.5 H29"/>
          </g>
        </svg>
        www.graceharbour.tv
      </span>
      <span class="footer-bar__item footer-bar__item--social">
        <svg class="footer-bar__icon" viewBox="0 0 34 34" aria-hidden="true">
          <circle cx="17" cy="17" r="15" fill="none" stroke="#ffffff" stroke-width="1.6"/>
        </svg>
        koaministries
      </span>
    </div>
  </div>
</body>
</html>
```